Poster Needed for Church Conference

I need a poster for a weekend conference at my church. Looking to attract as many people as possible. We are a church in the suburbs of Houston. This is mainly for our own church members but we are opening it up to outside church members.

Please see previous design from last conference and all other graphic work that can (doesn't need to be) included.

Target Market(s)

It's targeted for all people. But our main audience is families. around the age of 30 should be main target.

Industry/Entity Type

Non-Profit

Font styles to use
Serif
Sans Serif

Colors

Designer to choose colors to be used in the design.

Requirements
Must have
• 11x17 design with ability to shrink and blow up. but ideally for 11x17
• Content and wording:
• "Rooted Light Conference: Bridging the gap between generations and passing on our deepest beliefs and values."
• Featuring Dr. Gil Marsden. Author of "The Path of P4"
• Aug 25-26: Friday 8-10 pm, Saturday 4-8 pm
• Cost Adults $15/Children $5: Covers admission to all sessions and workshops, refreshments and Saturday dinner. *kids 5 and under free
• Childcare provided for all sessions. "
• Please use church logo and address on flyer: 4312 Route 19, Missouri City, TX 77988
Nice to have
• Ideally it will be designed so that we can crop a 16:9 pp announcement slide and header for our website.
Should not have
• anything offensive

```html
<!DOCTYPE html>
<html lang="en">
<head>
<meta charset="utf-8">
<title>Rooted Light Conference Poster</title>
<link href="https://fonts.googleapis.com/css2?family=Arvo:wght@700&family=Montserrat:wght@800&display=swap" rel="stylesheet">
<style>
  :root{
    --green:#5cbf48;
    --green-deep:#2f9a2c;
    --green-bright:#6fd34f;
    --charcoal:#333333;
    --ink:#2b2b2b;
    --orange:#f28c1a;
    --blue:#2a97e0;
    --blue-light:#4fb6f2;
    --paper:#f5f5f2;
    --white:#ffffff;
  }
  *{margin:0;padding:0;box-sizing:border-box}
  html,body{width:800px;height:1200px;overflow:hidden;background:var(--white)}
  .poster{
    position:absolute;left:0;top:0;width:791px;height:1220px;
    transform:scale(1.0114,0.9836);transform-origin:0 0;
    background:var(--paper);overflow:hidden;
    font-family:"Montserrat",Arial,sans-serif;
  }
  .serif{font-family:"Arvo",Georgia,serif;font-weight:700}
  .header{
    position:absolute;left:0;top:0;width:791px;height:405px;
    background:
      radial-gradient(ellipse at 70% 10%, rgba(255,255,255,.35), transparent 55%),
      linear-gradient(180deg,#4fbf3c 0%,#2c9c2a 55%,#3aa534 80%,#58c04a 100%);
  }
  .header-texture{
    position:absolute;left:0;top:300px;width:791px;height:105px;
    background:repeating-linear-gradient(90deg,rgba(255,255,255,.08) 0 14px,transparent 14px 40px);
  }
  .title-lead,.title-main{
    position:absolute;left:49px;color:var(--white);white-space:nowrap;
    text-shadow:2px 2px 3px rgba(0,0,0,.35);
  }
  .title-lead{top:60px;font-size:38px}
  .title-main{top:118px;font-size:52px;line-height:67px}
  .band-green{position:absolute;left:0;top:405px;width:791px;height:15px;background:var(--green-bright)}
  .band-dark{position:absolute;left:0;top:420px;width:791px;height:30px;background:var(--charcoal)}
  .feature{
    position:absolute;left:0;top:450px;width:791px;height:295px;
    background:linear-gradient(90deg,#fbfdf3 0%,#eaf3b0 40%,#a8c93a 75%,#6f8f24 100%);
  }
  .feature::after{
    content:"";position:absolute;left:0;top:260px;width:791px;height:35px;
    background:linear-gradient(90deg,rgba(255,255,255,.6),rgba(100,130,30,.5));
  }
  .featuring{position:absolute;left:66px;top:476px;font-size:26px;color:var(--ink)}
  .speaker{position:absolute;left:66px;top:516px;font-size:37px;font-weight:800;color:var(--green-deep);letter-spacing:.5px}
  .author{position:absolute;left:66px;top:562px;font-size:24px;color:var(--ink)}
  .photo{
    position:absolute;left:496px;top:397px;width:268px;height:323px;
    border:3px solid var(--white);border-radius:10px;
    background:radial-gradient(ellipse at 50% 45%,#9a7a66 0%,#4a3a32 40%,#111 75%);
    box-shadow:0 2px 6px rgba(0,0,0,.4);
  }
  .book{
    position:absolute;left:146px;top:618px;width:140px;height:190px;
    transform:rotate(6deg);
    background:linear-gradient(160deg,#ffffff 0%,#e8e8e8 60%,#d4d4d4 100%);
    border-bottom:18px solid var(--green);
    box-shadow:4px 6px 10px rgba(0,0,0,.3);
  }
  .details{position:absolute;left:0;top:745px;width:791px;height:293px;background:linear-gradient(180deg,#e9e9e4,#fafaf7)}
  .art{position:absolute;left:0;top:745px}
  .dates{position:absolute;left:66px;top:878px;font-size:27px;font-weight:800;line-height:36px;color:var(--ink)}
  .cost{position:absolute;left:518px;top:838px;width:210px;text-align:center;font-size:20px;font-weight:800;line-height:26px;color:var(--white)}
  .childcare{position:absolute;left:498px;top:958px;width:250px;text-align:center;font-size:15.5px;font-weight:800;line-height:21px;color:var(--ink)}
  .inclusions{
    position:absolute;left:0;top:1038px;width:604px;height:124px;background:var(--green);
  }
  .inclusions p{
    position:absolute;left:60px;top:22px;white-space:nowrap;
    font-size:19px;line-height:29px;color:var(--white);
  }
  .church-name{
    position:absolute;left:604px;top:1038px;width:187px;height:124px;background:var(--charcoal);
    display:flex;align-items:center;justify-content:center;text-align:center;
    font-size:22px;line-height:28px;color:var(--white);
  }
  .address{
    position:absolute;left:0;top:1162px;width:791px;height:58px;background:var(--charcoal);
    display:flex;align-items:center;justify-content:center;
    font-size:22px;color:var(--white);
  }
</style>
</head>
<body>
<div class="poster">
  <section class="header">
    <div class="header-texture"></div>
    <div class="title-lead serif">Rooted Light Conference:</div>
    <h1 class="title-main serif">Bridging the gap between<br>generations and passing<br>on our deepest beliefs<br>and values.</h1>
  </section>
  <div class="band-green"></div>
  <div class="band-dark"></div>

  <section class="feature"></section>
  <div class="featuring serif">Featuring</div>
  <div class="speaker">DR. GIL MARSDEN.</div>
  <div class="author serif">Author of "The Path of P4"</div>
  <div class="photo" role="img" aria-label="Portrait photo of the featured speaker"></div>

  <section class="details"></section>
  <svg class="art" width="791" height="293" viewBox="0 0 791 293">
    <defs>
      <linearGradient id="bannerGreen" x1="0" y1="0" x2="1" y2="0">
        <stop offset="0" stop-color="#c4dc2a"/>
        <stop offset="1" stop-color="#5fae2a"/>
      </linearGradient>
      <linearGradient id="ribbonBlue" x1="0" y1="0" x2="0" y2="1">
        <stop offset="0" stop-color="var(--blue-light)"/>
        <stop offset="1" stop-color="var(--blue)"/>
      </linearGradient>
    </defs>
    <path d="M0 40 C150 10 300 60 395 20 C380 80 400 160 441 230 C300 200 150 260 0 250 Z" fill="var(--orange)"/>
    <path d="M0 55 C150 25 300 70 385 35 C375 95 395 170 430 240 C290 210 150 275 0 262 Z" fill="url(#bannerGreen)"/>
    <polygon points="441,140 500,70 720,60 740,135 776,207 720,180 500,185" fill="#1c78bf"/>
    <polygon points="478,70 730,60 738,180 495,188" fill="url(#ribbonBlue)"/>
  </svg>
  <div class="book" role="img" aria-label="Cover of the book The Path of P4"></div>
  <div class="dates">AUG 25-26:<br>FRIDAY 8-10 PM,<br>SATURDAY 4-8 PM</div>
  <div class="cost">COST<br>ADULTS $15<br>CHILDREN $5</div>
  <div class="childcare">CHILDCARE PROVIDED<br>FOR ALL SESSIONS.</div>

  <section class="inclusions">
    <p class="serif">Covers admission to all sessions and<br>workshops, refreshments and Saturday<br>dinner. *kids 5 and under free</p>
  </section>
  <div class="church-name serif">Grace Vale<br>Church</div>
  <footer class="address serif">4312 Route 19, Missouri City, TX 77988</footer>
</div>
</body>
</html>
```